Redesign start page for existing online shop

We are selling building material (chimneys and flue pipes) as well as fireplaces (stoves). For this online shop we need a new start page. The domain is kaminwelt-versand.de. Here you can see the current design. We want a smoother design with just one banner in the middle instead of the three in the first row. The look has to be more professional and trustworthy. You can therefore play with the colors. We want to try some different orange instead of our yellow / orange color. A few more things: - The phone number has to be bigger and more highlighted - So the 5 advantages at the top should be shown in a different way - New design for the products below - New footer

Target Market(s)

Germany and other countries in Europe.

Industry/Entity Type

Home Builder

Number of Pages Required

1 page

Font styles to use
Other font styles liked:
• Please se the font on our current site.

Colors
f78f20
f68d4c

Requirements
Must have
• - Clear design - Trustworthy look - All elements Which are now shown shoulderstand be still there after redesigning -
Nice to have
• - See the Following sites to have a clou about our wishes: glutvia.de warmbrio.de

```html
<!DOCTYPE html>
<html lang="de">
<head>
<meta charset="utf-8">
<title>Kaminwelt Versand – Startseite</title>
<link rel="stylesheet" href="https://fonts.googleapis.com/css2?family=Open+Sans:wght@400;600;700;800&display=swap">
<style>
:root{
  --black:#0d0d0d;
  --white:#ffffff;
  --nav:#4b5b61;
  --slate:#364244;
  --footer:#242d31;
  --yellow:#f9d33d;
  --gold-text:#f6c443;
  --orange:#f78f20;
  --red:#c8141e;
  --ink:#2b2f33;
  --tag:#1f2b38;
}
*{margin:0;padding:0;box-sizing:border-box}
html,body{width:1200px;height:4276px;overflow:hidden}
body{position:relative;background:var(--white);font-family:"Open Sans",Arial,sans-serif;color:var(--ink)}
.abs{position:absolute}

/* top bar */
.topbar{left:0;top:0;width:1200px;height:45px;background:var(--black)}
.topbar-link{top:0;height:45px;display:flex;align-items:center;gap:10px;color:var(--white);font-size:12px}
.topbar-link svg{width:26px;height:26px}

/* header */
.header{left:0;top:45px;width:1200px;height:132px;background:var(--white)}
.brand{left:34px;top:84px;display:flex;align-items:center;gap:12px}
.brand-dot{width:40px;height:40px;border-radius:50%;background:var(--orange)}
.brand-name{font-size:22px;font-weight:700;line-height:24px;color:var(--ink);letter-spacing:.5px}
.search{left:598px;top:97px;width:200px;height:34px;border-radius:17px;background:var(--slate);display:flex;align-items:center;padding:0 12px 0 18px;justify-content:space-between}
.search span{font-size:10px;color:#cfd6d8}
.phone{left:855px;top:83px;display:flex;align-items:center;gap:14px}
.phone-number{font-size:31px;font-weight:700;color:var(--ink);letter-spacing:1.5px;line-height:34px}
.phone-hours{font-size:11px;font-weight:700;color:var(--ink);text-align:right;letter-spacing:.3px}

/* navigation */
.nav{left:0;top:177px;width:1200px;height:68px;background:var(--nav);display:flex;align-items:center}
.nav a{position:absolute;color:var(--white);text-decoration:none;font-size:19px;letter-spacing:1px}

/* hero */
.hero{left:0;top:245px;width:1200px;height:579px;background:linear-gradient(180deg,#9a9a9a 0%,#6e6e6e 45%,#3a3a3a 100%)}
.hero-title{left:0;top:500px;width:1200px;text-align:center;font-size:66px;font-weight:700;color:var(--white);letter-spacing:6px}

/* brands */
.brands{left:0;top:824px;width:1200px;height:108px;background:var(--yellow)}
.brands-label{left:197px;top:858px;font-size:15px;color:var(--red)}
.brand-partner{top:855px;display:flex;align-items:center;gap:8px;font-size:22px;font-weight:700;color:var(--red)}
.brand-partner i{display:block;width:22px;height:22px;background:var(--red)}

/* advantages */
.advantages{left:0;top:949px;width:1200px;height:550px;background:var(--slate)}
.advantage{top:1075px;width:260px;text-align:center}
.advantage svg{width:110px;height:110px;display:block;margin:0 auto}
.advantage h3{margin-top:26px;font-size:17px;font-weight:400;color:var(--gold-text);line-height:24px;min-height:48px}
.advantage p{margin-top:24px;font-size:15px;line-height:24px;color:var(--white)}

/* intro */
.intro-title{left:0;top:1588px;width:1200px;text-align:center;font-size:44px;font-weight:600;color:var(--orange)}
.intro-line{left:300px;top:1831px;font-size:30px;color:var(--ink)}
.btn{display:flex;align-items:center;justify-content:center;background:var(--red);color:var(--white);font-size:15px;font-weight:600}
.intro-btn{left:721px;top:1832px;width:177px;height:43px}

/* products */
.product-visual{background:linear-gradient(90deg,#c9cdd0,#f3f4f5 50%,#a9aeb2)}
.price{background:var(--tag);color:var(--white);font-size:13px;display:flex;align-items:center;justify-content:center}
.product-name{font-size:24px;line-height:30px;color:var(--ink)}
.view-btn{width:102px;height:52px;font-size:15px}

.photo-welding{left:388px;top:1990px;width:812px;height:700px;background:radial-gradient(circle at 62% 62%,#d8843a 0%,#6a4632 22%,#33302e 55%,#1f1f1f 100%)}
.photo-gears{left:0;top:2695px;width:810px;height:702px;background:radial-gradient(circle at 55% 55%,#e2c386 0%,#c9a561 45%,#8f733c 100%)}

/* footer */
.footer{left:0;top:3410px;width:1200px;height:866px;background:var(--footer)}
.footer-title{left:114px;top:3640px;font-size:22px;font-weight:600;line-height:32px;color:var(--gold-text)}
.footer-text{left:114px;top:3738px;font-size:15px;line-height:27px;color:var(--white)}
.footer-text-wide{left:114px;top:3950px;font-size:15px;line-height:27px;color:var(--white)}
</style>
</head>
<body>

<!-- top bar -->
<div class="abs topbar"></div>
<div class="abs topbar-link" style="left:935px">Mein Konto
  <svg viewBox="0 0 26 26" fill="none" stroke="#fff" stroke-width="1.5"><circle cx="13" cy="13" r="11"/><circle cx="13" cy="10" r="4"/><path d="M6 20c2-4 12-4 14 0"/></svg>
</div>
<div class="abs topbar-link" style="left:1058px">Warenkorb
  <svg viewBox="0 0 26 26" fill="none" stroke="#fff" stroke-width="1.5"><path d="M3 5h4l3 11h11l2-8H8"/><circle cx="11" cy="20" r="1.6"/><circle cx="19" cy="20" r="1.6"/></svg>
</div>

<!-- header -->
<header class="abs header"></header>
<div class="abs brand">
  <div class="brand-dot"></div>
  <div class="brand-name">KAMINWELT<br>VERSAND</div>
</div>
<div class="abs search">
  <span>Suchbegriff oder Artikelnummer</span>
  <svg width="18" height="18" viewBox="0 0 18 18" fill="none" stroke="#fff" stroke-width="2"><circle cx="7.5" cy="7.5" r="5.5"/><path d="M11.5 11.5l5 5"/></svg>
</div>
<div class="abs phone">
  <svg width="30" height="38" viewBox="0 0 30 38" fill="none" stroke="#2b2f33" stroke-width="2.4"><path d="M8 2l5 7-4 4c2 6 5 10 10 13l4-4 6 5-4 6C14 33 3 20 2 7z"/></svg>
  <div>
    <div class="phone-number">0821/447 318 0</div>
    <div class="phone-hours">MON - FRI 9:00 TO 6:00 P.M.</div>
  </div>
</div>

<!-- navigation -->
<nav class="abs nav">
  <a style="left:37px">ONLINE SHOP</a>
  <a style="left:222px">SERVICE</a>
  <a style="left:345px">STANDORTE I</a>
  <a style="left:504px">FÜR HÄNDLER I</a>
  <a style="left:690px">INSTALLATEURE</a>
</nav>

<!-- hero -->
<section class="abs hero" role="img" aria-label="Schwarzweißfoto einer Industrieanlage mit hohem Schornstein vor bewölktem Himmel"></section>
<h1 class="abs hero-title">SCHORNSTEIN</h1>

<!-- brands -->
<section class="abs brands"></section>
<div class="abs brands-label">Unsere Marken</div>
<div class="abs brand-partner" style="left:450px">Rauchwerk</div>
<div class="abs brand-partner" style="left:655px"><i></i>Falkenrohr</div>
<div class="abs brand-partner" style="left:870px"><i></i>Kessler + Brandt</div>

<!-- advantages -->
<section class="abs advantages"></section>
<div class="abs advantage" style="left:192px">
  <svg viewBox="0 0 110 110" fill="none" stroke="#f6c443" stroke-width="4" stroke-linejoin="round" stroke-linecap="round">
    <path d="M20 90l55-55"/><path d="M68 20l22 22-10 4-16-16z"/>
    <path d="M90 90L40 40"/><path d="M40 40c-10 4-20-4-18-14l8 6 6-4-2-10c10-2 18 8 14 18"/>
  </svg>
  <h3>Mounting Service</h3>
  <p>consectetuer adipiscing sed diam nonummy nibh euismod tincidunt ut laoreet dolore magna aliquam</p>
</div>
<div class="abs advantage" style="left:468px">
  <svg viewBox="0 0 110 110" fill="none" stroke="#f6c443" stroke-width="4" stroke-linejoin="round">
    <path d="M55 12l34 12v30c0 22-16 36-34 44C37 90 21 76 21 54V24z"/>
  </svg>
  <h3>Made in Germany<br>with 25 years warranty</h3>
  <p>erat volutpat Ut wisi enim ad minim veniam quis nostrud exerci tation</p>
</div>
<div class="abs advantage" style="left:776px">
  <svg viewBox="0 0 110 110" fill="none" stroke="#f6c443" stroke-width="4" stroke-linejoin="round" stroke-linecap="round">
    <rect x="20" y="14" width="58" height="80" rx="4"/>
    <path d="M30 32l5 5 8-9M50 33h18M30 52l5 5 8-9M50 53h18M30 72l5 5 8-9M50 73h10"/>
    <path d="M95 40L68 80l-6 6 2-9 27-39z"/>
  </svg>
  <h3>Free Advisement</h3>
  <p>ullamcorper suscipit lobortis nisl ut aliquip ex ea commodo consequat</p>
</div>

<!-- intro -->
<h2 class="abs intro-title">Anteposuerit Litterarum</h2>
<p class="abs intro-line">Lorem ipsum dolor sit amet</p>
<a class="abs btn intro-btn">Lorem Ipsum</a>

<!-- product row 1 -->
<div class="abs product-visual" style="left:184px;top:2010px;width:34px;height:200px" role="img" aria-label="Produktfoto: Edelstahl-Rauchrohr"></div>
<div class="abs price" style="left:214px;top:2160px;width:76px;height:30px">ab € 63,00</div>
<div class="abs product-name" style="left:54px;top:2263px">Consectetuer<br>adipiscing</div>
<a class="abs btn view-btn" style="left:262px;top:2268px">View</a>

<div class="abs product-visual" style="left:114px;top:2430px;width:186px;height:96px" role="img" aria-label="Produktfoto: Regenhaube aus Edelstahl"></div>
<div class="abs price" style="left:200px;top:2520px;width:98px;height:32px">ab € 116,50</div>
<div class="abs product-name" style="left:54px;top:2628px">laoreet dolore</div>
<a class="abs btn view-btn" style="left:262px;top:2616px">View</a>

<div class="abs photo-welding" role="img" aria-label="Foto: Handwerker beim Schleifen von Metall mit Funkenflug"></div>

<!-- product row 2 -->
<div class="abs photo-gears" role="img" aria-label="Goldgetöntes Foto: Zahnräder und Werkzeugteile"></div>

<div class="abs product-visual" style="left:898px;top:2750px;width:156px;height:130px" role="img" aria-label="Produktfoto: Dämmplatten für Kaminanschluss"></div>
<div class="abs price" style="left:1015px;top:2872px;width:80px;height:30px">ab € 99,90</div>
<div class="abs product-name" style="left:860px;top:2958px">Consectetuer<br>adipiscing</div>
<a class="abs btn view-btn" style="left:1076px;top:2970px">View</a>

<div class="abs" style="left:900px;top:3044px;width:160px;height:200px;background:linear-gradient(135deg,#3a3a3a,#111 60%,#2a2a2a)" role="img" aria-label="Produktfoto: schwarzes Ofenrohr-Knie"></div>
<div class="abs price" style="left:1015px;top:3228px;width:80px;height:30px">ab € 9,90</div>
<div class="abs product-name" style="left:860px;top:3327px">laoreet dolore</div>
<a class="abs btn view-btn" style="left:1076px;top:3315px">View</a>

<!-- footer -->
<footer class="abs footer"></footer>
<h3 class="abs footer-title">Magna aliquam erat volutpat Ut wisi enim<br>ad minim veniam quis nostrud exerci tation</h3>
<p class="abs footer-text">consectetuer adipiscing sed diam nonummy<br>nibh euismod tincidunt ut laoreet dolore<br>magna aliquam erat volutpat Ut wisi enim<br>ad minim veniam quis nostrud exerci tation<br>ullamcorper suscipit lobortis nisl ut aliquip ex<br>ea commodo consequat</p>
<p class="abs footer-text-wide">ad minim veniam quis nostrud exerci tation ullamcorper suscipit lobortis nisl ut aliquip ex ea commodo consequat<br>consectetuer adipiscing sed diam nonummy nibh euismod tincidunt ut laoreet dolore.</p>

</body>
</html>
```